Endocrinologist needs new stationery

I have a logo from MarkForge and now need stationery with the new logo.

Address: Suite 4, 282 Falcon Street, Richmond, VIC 3121
Phone: 03 9417 2253
Fax: 03 9417 2255
Website: www.drmaylacorwen.com.au
Email: admin@drmaylacorwen.com.au

```html
<!DOCTYPE html>
<html lang="en">
<head>
<meta charset="utf-8">
<title>Dr Mayla Corwen – Stationery</title>
<link rel="stylesheet" href="https://fonts.googleapis.com/css2?family=Arimo:wght@400;700&display=swap">
<style>
  :root {
    --backdrop: #e6e6e6;
    --paper: #ffffff;
    --brand-blue: #336a99;
    --brand-plum: #6f5166;
    --ink: #555555;
    --ink-dark: #333333;
    --rule: #9a9a9a;
    --shadow: 0 2px 5px rgba(0,0,0,.28);
  }
  * { box-sizing: border-box; margin: 0; padding: 0; }
  html, body { width: 1200px; height: 900px; overflow: hidden; }
  body { background: var(--backdrop); font-family: "Arimo", Arial, sans-serif; color: var(--ink); position: relative; }

  .sheet { position: absolute; background: var(--paper); box-shadow: var(--shadow); overflow: hidden; }
  .band { position: absolute; left: 0; bottom: 0; width: 100%; display: block; }

  .wordmark { position: absolute; font-weight: 400; color: var(--brand-blue); letter-spacing: .5px; white-space: nowrap; }
  .wordmark--light { color: var(--paper); }

  /* Letterhead */
  .letterhead { left: 40px; top: 91px; width: 507px; height: 716px; }
  .letterhead .wordmark { left: 28px; top: 52px; font-size: 22px; }
  .contact-block { position: absolute; border-left: 1px solid var(--rule); padding-left: 6px; font-size: 8.5px; line-height: 10.5px; color: var(--ink); font-style: normal; white-space: nowrap; }
  .letterhead .contact-block { left: 346px; top: 33px; }
  .contact-block .gap { height: 5px; }
  .icon { display: inline-block; width: 7px; height: 7px; vertical-align: -1px; margin-right: 2px; }
  .salutation { position: absolute; left: 47px; top: 220px; font-size: 11px; font-weight: 700; color: var(--ink-dark); }
  .letter-body { position: absolute; left: 46px; top: 253px; width: 418px; font-size: 8.2px; line-height: 10.2px; color: var(--ink-dark); }
  .letter-body p { margin-bottom: 8px; }
  .sign-off { position: absolute; left: 47px; top: 469px; font-size: 6px; font-weight: 700; color: var(--ink-dark); }
  .signature { position: absolute; left: 46px; top: 497px; width: 84px; height: 22px; background: linear-gradient(90deg, #cfcfcf, #e8e8e8); border-radius: 3px; }

  /* Business card front */
  .card-front { left: 578px; top: 91px; width: 281px; height: 160px; }
  .card-front .wordmark { left: 0; width: 281px; text-align: center; top: 24px; font-size: 18px; }
  .card-name { position: absolute; right: 147px; top: 86px; text-align: right; }
  .card-name strong { display: block; font-size: 10px; color: var(--brand-blue); font-weight: 700; }
  .card-name span { display: block; font-size: 7.5px; letter-spacing: .3px; color: var(--ink); margin-top: 1px; }
  .card-front .contact-block { left: 140px; top: 76px; font-size: 8px; line-height: 10px; }
  .card-address { position: absolute; left: 0; width: 281px; top: 131px; text-align: center; font-size: 7.5px; color: var(--ink); }

  /* Business card back */
  .card-back { left: 879px; top: 91px; width: 281px; height: 160px; background: var(--brand-blue); }
  .card-back .pattern { position: absolute; inset: 0; background: linear-gradient(135deg, #3a72a2, #30648f); }
  .card-back .wordmark { left: 0; width: 281px; text-align: center; top: 66px; font-size: 18px; }

  /* Envelope front */
  .envelope-front { left: 578px; top: 277px; width: 582px; height: 253px; }
  .envelope-front .wordmark { left: 19px; top: 22px; font-size: 20px; }
  .return-address { position: absolute; left: 20px; top: 60px; font-size: 8.5px; line-height: 10.5px; color: var(--ink); }

  /* Envelope back */
  .envelope-back { left: 578px; top: 556px; width: 582px; height: 252px; }
  .flap { position: absolute; left: 0; top: 0; display: block; }
  .envelope-back .wordmark { left: 0; width: 582px; text-align: center; top: 23px; font-size: 19px; }
</style>
</head>
<body>

<!-- Letterhead -->
<section class="sheet letterhead">
  <div class="wordmark">Dr Mayla Corwen</div>
  <address class="contact-block">
    <div>Suite 4, 282 Falcon Street</div>
    <div>Ashvale, VIC 3187</div>
    <div class="gap"></div>
    <div><svg class="icon" viewBox="0 0 10 10"><path d="M2 1h2l1 2.5-1.3 1a6 6 0 0 0 2.8 2.8l1-1.3L10 7v2H8A7 7 0 0 1 1 2V1z" fill="#555"/></svg>03 9417 2253</div>
    <div><svg class="icon" viewBox="0 0 10 10"><rect x="1" y="4" width="8" height="5" fill="#555"/><rect x="3" y="1" width="4" height="3" fill="#555"/></svg>03 9417 2255</div>
    <div><svg class="icon" viewBox="0 0 10 10"><rect x="0.5" y="2" width="9" height="6" fill="#555"/><path d="M1 2.5l4 3 4-3" stroke="#fff" fill="none"/></svg>admin@drmaylacorwen.com.au</div>
    <div><svg class="icon" viewBox="0 0 10 10"><circle cx="5" cy="5" r="4.5" fill="#555"/><path d="M0.5 5h9M5 0.5c-2 2.5-2 6.5 0 9M5 0.5c2 2.5 2 6.5 0 9" stroke="#fff" stroke-width=".7" fill="none"/></svg>www.drmaylacorwen.com.au</div>
  </address>

  <h1 class="salutation">Dear Mr. Hale,</h1>
  <div class="letter-body">
    <p>Lorem ipsum dolor sit amet, consectetuer adipiscing elit, sed diam nonmmy nibh euismod tincidunt ut laor eet dolore magna aliquam erat volutpat. Ut wisi enim ad minim veniam, quis nostrud exerci tationmcorper suscipit lobortis nisl ut aliquip ex ea commodo consequat. Duis autem vel eum iriure dolor in hendrerit in vulputate velit esse molestie consequat, vel illum dolore eu feugiat</p>
    <p>Rorem ipsum dolor sit amet, consectetuer adipiscing elit, sed diam nonmmy nibh euismod tincidunt ut laor eet dolore magna aliquam erat volutpat. Ut wisi enim ad minim veniam, quis nostrud exerci tationmcorper suscipit lobortis nisl ut aliquip ex ea commodo consequat. Duis autem vel eum iriure dolor in hendrerit in vulputate velit esse molest</p>
    <p>Dorem ipsum dolor sit amet, consectetuer adipiscing elit, sed diam nonmmy nibh euismod tincidunt ut laor eet dolore magna aliquam erat volutpat. Ut wisi enim ad minim veniam, quis nostrud exerci tationmcorper suscipit lobortis nisl ut aliquip ex ea commodo consequat. Duis autem vel eum iriure dolor in hendrerit in vulputate velit esse molestie consequat, vel illum</p>
    <p>Sorem ipsum dolor sit amet, consectetuer adipiscing elit, sed diam nonmmy nibh euismod tincidunt ut laor eet dolore magna aliquam erat volutpat. Ut wisi enim ad minim veniam, quis nostrud exerci tationmcorper suscipit lobortis nisl ut aliquip ex ea commodo consequat. Duis autem vel eum iriure dolor in</p>
  </div>
  <div class="sign-off">Sincerely,</div>
  <div class="signature" role="img" aria-label="Handwritten signature"></div>

  <svg class="band" width="507" height="18" viewBox="0 0 507 18">
    <polygon points="0,0 256,0 246,18 0,18" fill="var(--brand-blue)"/>
    <polygon points="265,0 507,0 507,18 255,18" fill="var(--brand-plum)"/>
  </svg>
</section>

<!-- Business card, front -->
<section class="sheet card-front">
  <div class="wordmark">Dr Mayla Corwen</div>
  <div class="card-name"><strong>DR MAYLA CORWEN</strong><span>ENDOCRINOLOGY</span></div>
  <div class="contact-block">
    <div><svg class="icon" viewBox="0 0 10 10"><path d="M2 1h2l1 2.5-1.3 1a6 6 0 0 0 2.8 2.8l1-1.3L10 7v2H8A7 7 0 0 1 1 2V1z" fill="#555"/></svg>03 9417 2253</div>
    <div><svg class="icon" viewBox="0 0 10 10"><rect x="1" y="4" width="8" height="5" fill="#555"/><rect x="3" y="1" width="4" height="3" fill="#555"/></svg>03 9417 2255</div>
    <div><svg class="icon" viewBox="0 0 10 10"><rect x="0.5" y="2" width="9" height="6" fill="#555"/><path d="M1 2.5l4 3 4-3" stroke="#fff" fill="none"/></svg>admin@drmaylacorwen.com.au</div>
    <div><svg class="icon" viewBox="0 0 10 10"><circle cx="5" cy="5" r="4.5" fill="#555"/><path d="M0.5 5h9M5 0.5c-2 2.5-2 6.5 0 9M5 0.5c2 2.5 2 6.5 0 9" stroke="#fff" stroke-width=".7" fill="none"/></svg>www.drmaylacorwen.com.au</div>
  </div>
  <div class="card-address">Suite 4, 282 Falcon Street, Ashvale, VIC 3187</div>
  <svg class="band" width="281" height="10" viewBox="0 0 281 10">
    <polygon points="0,0 144,0 138,10 0,10" fill="var(--brand-blue)"/>
    <polygon points="148,0 281,0 281,10 142,10" fill="var(--brand-plum)"/>
  </svg>
</section>

<!-- Business card, back -->
<section class="sheet card-back">
  <div class="pattern" role="img" aria-label="Faint repeated name pattern in blue tones"></div>
  <div class="wordmark wordmark--light">Dr Mayla Corwen</div>
</section>

<!-- Envelope, front -->
<section class="sheet envelope-front">
  <div class="wordmark">Dr Mayla Corwen</div>
  <div class="return-address">Suite 4, 282 Falcon Street<br>Ashvale, VIC 3187</div>
  <svg class="band" width="582" height="21" viewBox="0 0 582 21">
    <polygon points="0,0 292,0 282,21 0,21" fill="var(--brand-blue)"/>
    <polygon points="302,0 582,0 582,21 291,21" fill="var(--brand-plum)"/>
  </svg>
</section>

<!-- Envelope, back -->
<section class="sheet envelope-back">
  <svg class="flap" width="582" height="72" viewBox="0 0 582 72">
    <path d="M0,0 H582 L570,40 Q562,70 530,70 H52 Q20,70 12,40 Z" fill="var(--brand-blue)"/>
  </svg>
  <div class="wordmark wordmark--light">Dr Mayla Corwen</div>
</section>

</body>
</html>
```